Night Dresses business cards business requirers

We are a new company initiating Mexico operations. Our core business is Night woman dress (both formal and party dress) for rent. Gownhaven is the name of the company. ITS Gownhaven form by two word. The dress word and topia (Utopic) so the place Gownhaven Means That You cant get the ideal, perfect and unique dress for your event. So we would like a modern, very creative, and attractive business card.

Industry/Entity Type

Womens Clothing

Contact Information for Business Card

Rounded Borders, two faces

Requirements
Must have
• Rounded borders, logo and slogan, modern, glam, attractive design
Should not have
• modern design classic or not

```html
<!DOCTYPE html>
<html lang="en">
<head>
<meta charset="utf-8">
<title>Gownhaven – Business Card</title>
<link rel="stylesheet" href="https://fonts.googleapis.com/css2?family=Open+Sans:wght@400;600&display=swap">
<style>
  :root {
    --backdrop: #e9e6e2;
    --card-white: #ffffff;
    --card-black: #2a2a2b;
    --brand-pink: #b0579b;
    --ink-dark: #444446;
    --ink-grey: #4b4b4d;
    --emboss-grey: #5e5e60;
  }
  * { box-sizing: border-box; margin: 0; padding: 0; }
  html, body {
    width: 1200px; height: 1000px; overflow: hidden;
    background: var(--backdrop);
    font-family: "Open Sans", Arial, sans-serif;
  }
  .canvas { position: relative; width: 1200px; height: 1000px; }

  .card {
    position: absolute; left: 266px; width: 666px; height: 397px;
    border-radius: 28px;
    box-shadow: 0 3px 10px rgba(0,0,0,0.18);
  }
  .card--front { top: 74px; background: var(--card-white); }
  .card--back { top: 533px; background: var(--card-black); }

  .brand {
    position: absolute; transform: translateX(-50%);
    display: flex; flex-direction: column; align-items: center;
    white-space: nowrap;
  }
  .card--front .brand { left: 182px; top: 228px; }
  .brand__name {
    font-size: 29px; font-weight: 400;
    letter-spacing: 6px; color: var(--ink-grey); line-height: 1;
    padding-left: 6px;
  }
  .brand__tagline {
    margin-top: 7px; display: flex; align-items: center; gap: 8px;
    font-size: 14px; font-weight: 600;
    letter-spacing: 3px; color: var(--ink-grey); line-height: 1;
  }
  .brand__tagline::before, .brand__tagline::after {
    content: ""; width: 24px; height: 2px; background: currentColor;
  }
  .brand__tagline::after { margin-left: -3px; }

  .divider {
    position: absolute; left: 354px; top: 101px;
    width: 2px; height: 192px; background: var(--brand-pink);
  }

  .contact { position: absolute; left: 397px; top: 96px; color: var(--ink-dark); }
  .contact__name {
    font-size: 21px; font-weight: 600; color: var(--brand-pink);
    letter-spacing: 0.3px; line-height: 1.2;
  }
  .contact__title { font-size: 16px; line-height: 1.4; }
  .contact__address { margin-top: 20px; font-size: 16px; line-height: 24px; }
  .contact__lines { margin-top: 9px; list-style: none; }
  .contact__line {
    display: flex; align-items: center; gap: 7px;
    font-size: 16px; line-height: 25px;
  }
  .contact__icon { width: 15px; height: 15px; fill: var(--brand-pink); flex: none; }

  .card--back .brand { left: 333px; top: 252px; }
  .card--back .brand__name {
    font-size: 40px; letter-spacing: 9px;
    color: var(--emboss-grey); padding-left: 9px;
  }
  .card--back .brand__tagline {
    margin-top: 10px; gap: 11px; font-size: 19px; letter-spacing: 5px;
    color: var(--emboss-grey);
  }
  .card--back .brand__tagline::before,
  .card--back .brand__tagline::after { width: 34px; }
  .card--back .brand__tagline::after { margin-left: -5px; }
</style>
</head>
<body>
<main class="canvas">
  <section class="card card--front" aria-label="Business card front">
    <div class="brand">
      <p class="brand__name">GOWNHAVEN</p>
      <p class="brand__tagline">GOWNS TO LOAN</p>
    </div>

    <div class="divider"></div>

    <div class="contact">
      <p class="contact__name">LENA MORAVEC</p>
      <p class="contact__title">Managing Director/CEO</p>
      <p class="contact__address">2148 North Alder Lane<br>Westbrook, ME 04092</p>
      <ul class="contact__lines">
        <li class="contact__line">
          <svg class="contact__icon" viewBox="0 0 16 16" aria-hidden="true"><path d="M1 6c0-2 3-3.5 7-3.5S15 4 15 6v1.2h-3.2V5.8c-1-.4-2.4-.6-3.8-.6s-2.8.2-3.8.6v1.4H1z"/><path d="M3 8.5 5 6.5h6l2 2V14H3z"/></svg>
          <span>+ 000 000 0000</span>
        </li>
        <li class="contact__line">
          <svg class="contact__icon" viewBox="0 0 16 16" aria-hidden="true"><path d="M1 3.5h14v1L8 9 1 4.5z"/><path d="M1 6l7 4.5L15 6v6.5H1z"/></svg>
          <span>info@gownhaven.com</span>
        </li>
        <li class="contact__line">
          <svg class="contact__icon" viewBox="0 0 16 16" aria-hidden="true"><circle cx="8" cy="8" r="6.5" fill="none" stroke="var(--brand-pink)" stroke-width="1.6"/><path d="M1.5 8h13M8 1.5c2.2 2 2.2 11 0 13M8 1.5c-2.2 2-2.2 11 0 13" fill="none" stroke="var(--brand-pink)" stroke-width="1.2"/></svg>
          <span>www.gownhaven.com</span>
        </li>
      </ul>
    </div>
  </section>

  <section class="card card--back" aria-label="Business card back">
    <div class="brand">
      <p class="brand__name">GOWNHAVEN</p>
      <p class="brand__tagline">GOWNS TO LOAN</p>
    </div>
  </section>
</main>
</body>
</html>
```